Construction Company Needs Letterhead Design

We recently had a new logo designed and would like to have our letterhead updated to a trendier design. We are a concrete construction company based out of Iowa, but do work for Agricultural businesses across the Midwest.

Industry/Entity Type

Construction

Colors
ec1f27
000000
ffffff

Requirements
Must have
• Must stay within our current color scheme of red/black/white. Must have have our address, phone number, e-mail address, etc. printed on the letterhead as well.

```html
<!DOCTYPE html>
<html lang="en">
<head>
<meta charset="utf-8">
<title>Keston Farm Labor Services — Letterhead</title>
<link href="https://fonts.googleapis.com/css2?family=Lato:wght@400;700;900&display=swap" rel="stylesheet">
<style>
  :root {
    --brand-red: #ec1f27;
    --ink: #231f20;
    --band-grey: #8a8a8a;
    --paper: #ffffff;
    --backdrop: #dcdde0;
  }
  html, body {
    margin: 0;
    padding: 0;
    width: 970px;
    height: 1200px;
    overflow: hidden;
    background: var(--backdrop);
    font-family: "Lato", Arial, sans-serif;
  }
  .letterhead {
    position: absolute;
    left: 21px;
    top: 0;
    width: 927px;
    height: 1200px;
    background: var(--paper);
  }
  .masthead {
    position: absolute;
    top: 60px;
    left: 0;
    right: 0;
    display: flex;
    justify-content: center;
    align-items: center;
    gap: 14px;
  }
  .masthead-square {
    width: 40px;
    height: 40px;
    background: var(--brand-red);
  }
  .company-name {
    font-weight: 900;
    font-size: 34px;
    letter-spacing: 1px;
    color: var(--ink);
    text-transform: uppercase;
    line-height: 1;
  }
  .footer-rule {
    position: absolute;
    left: 0;
    right: 0;
    top: 1119px;
    height: 5px;
    background: var(--band-grey);
  }
  .footer-band {
    position: absolute;
    left: 0;
    right: 0;
    top: 1124px;
    bottom: 0;
    background: var(--ink);
  }
  .contact {
    position: absolute;
    top: 1095px;
    width: 240px;
    margin-left: -120px;
    text-align: center;
    color: var(--paper);
    font-size: 13px;
    font-weight: 700;
    line-height: 17px;
  }
  .contact-badge {
    display: block;
    width: 38px;
    height: 44px;
    margin: 0 auto 14px;
  }
  .contact-address { left: 198px; }
  .contact-phone { left: 463px; }
  .contact-web { left: 729px; }
  .contact p { margin: 0; }
</style>
</head>
<body>
  <main class="letterhead">
    <header class="masthead">
      <span class="masthead-square" aria-hidden="true"></span>
      <span class="company-name">Keston Farm Labor Services</span>
    </header>

    <div class="footer-rule"></div>
    <footer class="footer-band"></footer>

    <div class="contact contact-address">
      <svg class="contact-badge" viewBox="0 0 38 44" aria-hidden="true">
        <polygon points="19,0 38,11 38,33 19,44 0,33 0,11" fill="var(--brand-red)"/>
        <path d="M19 12c-4 0-7 3-7 7 0 5 7 12 7 12s7-7 7-12c0-4-3-7-7-7z" fill="#fff"/>
        <circle cx="19" cy="19" r="2.6" fill="var(--brand-red)"/>
      </svg>
      <p>4720 County Road K-14</p>
      <p>Milford, IA 50000</p>
    </div>

    <div class="contact contact-phone">
      <svg class="contact-badge" viewBox="0 0 38 44" aria-hidden="true">
        <polygon points="19,0 38,11 38,33 19,44 0,33 0,11" fill="var(--brand-red)"/>
        <path d="M14 13l3 -1 2.5 5 -2 1.5c1 2.5 3 4.5 5.5 5.5l1.5-2 5 2.5 -1 3c-8 0.5-15-6.5-14.5-14.5z" fill="#fff"/>
      </svg>
      <p>tel: (555) 010-4823</p>
      <p>fax: (555) 010-4829</p>
    </div>

    <div class="contact contact-web">
      <svg class="contact-badge" viewBox="0 0 38 44" aria-hidden="true">
        <polygon points="19,0 38,11 38,33 19,44 0,33 0,11" fill="var(--brand-red)"/>
        <rect x="11" y="16" width="16" height="12" fill="#fff"/>
        <path d="M11 16l8 6 8-6" fill="none" stroke="var(--brand-red)" stroke-width="1.4"/>
      </svg>
      <p>info@kestonconcrete.com</p>
      <p>www.kestonconcrete.com</p>
    </div>
  </main>
</body>
</html>
```